Innovative, creative, and beautiful simple book cover!

I’ve spend 5 years writing a book about executive consulting. Last task of the project is to find the best possible cover and I need help from you guys.

In the book, I take the liberty of creating a model which secures successful sales throughout the value chain, driven by the top management.

For you info, I used Pixel Harbor once before and of cause ended buying a logo. In short I’m here to buy the best book cover idea - and look forward to see what genius ideas you can bring to the table.

Thank you very much.
Torvald

P.S. Please see my brief in attach documents. .
Updates

Target Market(s)

Business people en general

Industry/Entity Type

Management Consulting

Font styles to use
Sans Serif

Requirements
Must have
• - My attach files about description for front page and back page have to be incorporated.
• - BOTH A FRONT, SPINE AND A BACK PAGE!
• - Please see all my attach files – the project is very well described and should be ready to work on.
• - The idea about the “building line” is an idea I love, but if you have something else you think I should see – try me.
Nice to have
• I love simple, minimalistic design
Should not have
• I don't like old fashion or over designed solutions. Sorry :-)

```html
<!DOCTYPE html>
<html lang="en">
<head>
<meta charset="utf-8">
<title>Strategic Deals Momentum – Book Cover</title>
<link rel="stylesheet" href="https://fonts.googleapis.com/css2?family=Archivo+Black&display=swap">
<style>
  :root {
    --backdrop: #d9d9d6;
    --cover-blue-deep: #17549e;
    --cover-blue: #1f86cc;
    --cover-blue-light: #2a97d8;
    --paper-white: #f7f7f8;
    --paper-grey: #dcdde0;
    --ink-blue: #1e7cc4;
    --title-white: #ffffff;
  }
  * { margin: 0; padding: 0; box-sizing: border-box; }
  html, body {
    width: 1200px;
    height: 780px;
    overflow: hidden;
    background: var(--backdrop);
  }
  .canvas {
    position: relative;
    width: 1200px;
    height: 780px;
  }
  .book-cover {
    position: absolute;
    left: 330px;
    top: 30px;
    width: 540px;
    height: 720px;
    overflow: hidden;
    background: linear-gradient(180deg, var(--paper-white) 0%, var(--paper-grey) 100%);
    box-shadow: 0 6px 18px rgba(0, 0, 0, 0.18);
    font-family: "Archivo Black", "Arial Black", sans-serif;
  }
  .cover-sky {
    position: absolute;
    left: 0;
    top: 0;
    width: 100%;
    height: 450px;
    background: linear-gradient(180deg, var(--cover-blue-deep) 0%, var(--cover-blue) 65%, var(--cover-blue-light) 100%);
  }
  .cover-title {
    position: absolute;
    left: 54px;
    top: 128px;
    color: var(--title-white);
    text-transform: uppercase;
    line-height: 0.88;
    letter-spacing: -1px;
  }
  .cover-title span { display: block; }
  .title-top { font-size: 50px; }
  .title-main { font-size: 100px; letter-spacing: -2px; }
  .title-bottom { font-size: 50px; }
  .skyline-band {
    position: absolute;
    left: 0;
    top: 450px;
    width: 100%;
    height: 90px;
    background: linear-gradient(180deg, var(--cover-blue-light) 0%, rgba(42, 151, 216, 0.45) 60%, rgba(42, 151, 216, 0) 100%);
  }
  .byline {
    position: absolute;
    right: 36px;
    top: 580px;
    text-align: center;
    color: var(--ink-blue);
    text-transform: uppercase;
  }
  .byline-label {
    display: block;
    font-size: 15px;
    letter-spacing: 0.5px;
    margin-bottom: 2px;
  }
  .byline-name {
    display: block;
    font-size: 32px;
    letter-spacing: -0.5px;
    white-space: nowrap;
  }
</style>
</head>
<body>
<main class="canvas">
  <section class="book-cover">
    <div class="cover-sky"></div>
    <h1 class="cover-title">
      <span class="title-top">Strategic</span>
      <span class="title-main">Deals</span>
      <span class="title-bottom">Momentum</span>
    </h1>
    <div class="skyline-band" role="img" aria-label="Blue silhouetted city skyline of landmark towers and buildings running across the cover"></div>
    <p class="byline">
      <span class="byline-label">Written by</span>
      <span class="byline-name">Torvald Brenholm</span>
    </p>
  </section>
</main>
</body>
</html>
```